Business Card Design

Copper Reef Coach Lines, name was derived from the Copper Reef jack (fish). We are a school bus charter service that offers supplemental bus transportation to district schools for field trips, school sporting events, etc. We also offer bus service to recreation centers during summer time for field trips.
Our business incorporates the color sea or royal blue, school bus yellow and a dark or charcoal gray. Its a copy of the fish's natural color scheme.

I am looking for a logo with the color scheme listed. I am looking for something modern and professional.

Target Market(s)

School Administrators, City employees

Industry/Entity Type

Recreation

Contact Information for Business Card

Copper Reef Coach Lines LLC
Safe Reliable Affordable
Dennis Harplomack, Owner
P.O.BOX 28617
St. Petersburg, Fl 33719
727-555-0193
www.ridecopperreef.example
ridecopperreef@mailbox.example

Requirements
Should not have
• pictures of fish or buses

```html
<!DOCTYPE html>
<html lang="en">
<head>
<meta charset="utf-8">
<title>Copper Reef Coach Lines – Business Card</title>
<link rel="stylesheet" href="https://fonts.googleapis.com/css2?family=Bebas+Neue&display=swap">
<style>
  :root {
    --card-teal: #1b3d48;
    --bus-yellow: #f7c600;
    --tag-gold: #c9962b;
    --label-gray: #74868c;
    --divider: #4d6770;
    --white: #ffffff;
  }
  html, body {
    margin: 0;
    width: 1200px;
    height: 702px;
    overflow: hidden;
    background: var(--card-teal);
  }
  .card {
    position: relative;
    width: 1200px;
    height: 702px;
    background: var(--card-teal);
    font-family: "Bebas Neue", "Oswald", sans-serif;
  }
  .brand-name {
    position: absolute;
    right: 75px;
    top: 150px;
    margin: 0;
    font-size: 106px;
    line-height: 1;
    font-weight: 400;
    color: var(--white);
    letter-spacing: 0.5px;
    white-space: nowrap;
  }
  .tagline {
    position: absolute;
    right: 77px;
    top: 254px;
    margin: 0;
    font-size: 22px;
    letter-spacing: 10.5px;
    color: var(--tag-gold);
    white-space: nowrap;
  }
  .owner {
    position: absolute;
    left: 0;
    width: 556px;
    top: 532px;
    text-align: center;
  }
  .owner-name {
    margin: 0;
    font-size: 44px;
    line-height: 1;
    letter-spacing: 3px;
    color: var(--bus-yellow);
  }
  .owner-title {
    margin: 10px 0 0;
    font-size: 26px;
    line-height: 1;
    letter-spacing: 2px;
    color: var(--bus-yellow);
  }
  .divider {
    position: absolute;
    left: 583px;
    top: 500px;
    width: 1px;
    height: 126px;
    background: var(--divider);
  }
  .contact {
    position: absolute;
    right: 84px;
    top: 508px;
    margin: 0;
    padding: 0;
    list-style: none;
    text-align: right;
  }
  .contact li {
    font-size: 22px;
    line-height: 30px;
    letter-spacing: 1.2px;
    color: var(--bus-yellow);
    white-space: nowrap;
  }
  .contact .label {
    color: var(--label-gray);
    margin-right: 8px;
  }
</style>
</head>
<body>
  <main class="card">
    <h1 class="brand-name">Copper Reef Coach Lines LLC</h1>
    <p class="tagline">Safe-Reliable-Affordable</p>

    <section class="owner">
      <p class="owner-name">Dennis Harplomack</p>
      <p class="owner-title">Owner</p>
    </section>

    <div class="divider"></div>

    <ul class="contact">
      <li><span class="label">Phone</span>727-555-0193</li>
      <li><span class="label">Add</span>P.O.BOX 28617 St. Petersburg, FL 33719</li>
      <li><span class="label">Mail</span>RIDECOPPERREEF@MAILBOX.EXAMPLE</li>
      <li><span class="label">Web</span>WWW.RIDECOPPERREEF.EXAMPLE</li>
    </ul>
  </main>
</body>
</html>
```